Storefront Sign Design for Rental Company

8ft x 8ft sign for the road in front of my business. I need something simple and clean but professional
Updates

Need extra days to review

Target Market(s)

Potential renters

Industry/Entity Type

Car Rental

Font styles to use
Serif
Sans Serif

Requirements
Must have
• Logo
• 555-207-1968
• MarvaleBreezeRental.com
• or
• www.MarvaleBreezeRental.com
• or
• MARVALEBREEZERENTAL.COM
• whichever looks better
Nice to have
• There is many cars that drive by each day so I would like something that shows my logo, phone number, and website

```html
<!DOCTYPE html>
<html lang="en">
<head>
<meta charset="utf-8">
<title>Marvale Breeze Rental – Car Rental Sign</title>
<link rel="stylesheet" href="https://fonts.googleapis.com/css2?family=Arimo:wght@700&display=swap">
<style>
  :root {
    --paper: #ffffff;
    --ink: #0b0b0b;
    --steel: #b9babc;
    --steel-dark: #8e8f92;
    --headline: #58595b;
    --floor: #d7d8da;
    --floor-dark: #8b8c90;
  }
  * { margin: 0; padding: 0; box-sizing: border-box; }
  html, body { width: 1200px; height: 1200px; overflow: hidden; background: var(--paper); }
  body { font-family: "Arimo", Arial, sans-serif; font-weight: 700; }
  .sign { position: relative; width: 1200px; height: 1200px; background: var(--paper); }
  .sign-frame { position: absolute; inset: 0; }
  .brand-name {
    position: absolute; left: 0; width: 1200px; top: 140px;
    text-align: center; color: var(--paper);
    font-size: 40px; line-height: 46px; letter-spacing: 6px;
  }
  .headline-main, .headline-sub {
    position: absolute; left: 0; width: 1200px; text-align: center;
    color: var(--headline); letter-spacing: -4px;
  }
  .headline-main { top: 385px; font-size: 274px; line-height: 274px; }
  .headline-sub { top: 614px; font-size: 123px; line-height: 123px; letter-spacing: -1px; }
  .headline-rule {
    position: absolute; left: 354px; top: 737px; width: 490px; height: 7px;
    background: var(--headline);
  }
  .keys-art {
    position: absolute; left: 578px; top: 740px; width: 44px; height: 72px;
    background: linear-gradient(180deg, #c9ccd1 0%, #2f3a48 45%, #aeb3ba 100%);
    border-radius: 10px;
  }
  .fleet-art {
    position: absolute; left: 96px; top: 862px; width: 1000px; height: 172px;
    background: linear-gradient(180deg, #ffffff 0%, #e6e6e8 48%, var(--floor-dark) 100%);
  }
  .contact { position: absolute; left: 0; top: 1054px; height: 60px; width: 1200px; color: var(--paper); }
  .contact-phone {
    position: absolute; left: 262px; top: 2px; font-size: 56px; line-height: 56px; letter-spacing: 0;
  }
  .contact-divider { position: absolute; left: 643px; top: 0; width: 2px; height: 60px; background: #9a9a9a; }
  .contact-web {
    position: absolute; left: 686px; top: 18px; font-size: 22px; line-height: 24px;
  }
  .icon { position: absolute; }
  .icon-phone { left: 212px; top: 14px; }
  .icon-globe { left: 660px; top: 22px; }
</style>
</head>
<body>
<main class="sign">
  <svg class="sign-frame" width="1200" height="1200" viewBox="0 0 1200 1200" aria-hidden="true">
    <defs>
      <linearGradient id="steel" x1="0" y1="0" x2="1" y2="1">
        <stop offset="0" stop-color="#e4e5e7"/>
        <stop offset="0.5" stop-color="#9c9da0"/>
        <stop offset="1" stop-color="#d9dadc"/>
      </linearGradient>
      <radialGradient id="glow" cx="0.5" cy="0.5" r="0.6">
        <stop offset="0" stop-color="#ffffff"/>
        <stop offset="0.7" stop-color="#f7f7f7"/>
        <stop offset="1" stop-color="#dcdcdd"/>
      </radialGradient>
    </defs>
    <rect class="panel" x="28" y="28" width="1144" height="1144" fill="var(--ink)"/>
    <polygon class="panel-bevel" points="44,28 1156,28 1008,596 1172,1172 28,1172 192,596" fill="url(#steel)"/>
    <polygon class="panel-light" points="60,28 1140,28 1000,596 1158,1172 42,1172 200,596" fill="url(#glow)"/>
    <polygon class="crest-edge" points="170,28 1030,28 1068,124 598,364 132,124" fill="url(#steel)"/>
    <polygon class="crest" points="176,28 1024,28 1062,120 598,356 138,120" fill="var(--ink)"/>
    <polygon class="footer-edge" points="90,1026 1044,1026 1136,1142 108,1142" fill="url(#steel)"/>
    <polygon class="footer-band" points="96,1030 1040,1032 1128,1140 110,1140" fill="var(--ink)"/>
  </svg>

  <div class="brand-name">MARVALE BREEZE<br>RENTAL</div>

  <div class="headline-main">CAR</div>
  <div class="headline-sub">RENTAL</div>
  <div class="headline-rule"></div>

  <div class="keys-art" role="img" aria-label="Illustration of a pair of car keys on a ring"></div>
  <div class="fleet-art" role="img" aria-label="Illustration of four sports cars in silver, purple, green and red parked in a showroom row"></div>

  <div class="contact">
    <svg class="icon icon-phone" width="34" height="34" viewBox="0 0 24 24" fill="none" stroke="#bfbfbf" stroke-width="1.4" aria-hidden="true">
      <path d="M5 3h4l2 5-2.5 1.5a11 11 0 0 0 6 6L16 13l5 2v4a2 2 0 0 1-2 2A16 16 0 0 1 3 5a2 2 0 0 1 2-2z"/>
      <path d="M15 3a6 6 0 0 1 6 6M15 6.5a2.5 2.5 0 0 1 2.5 2.5"/>
    </svg>
    <div class="contact-phone">555-207-1968</div>
    <div class="contact-divider"></div>
    <svg class="icon icon-globe" width="18" height="18" viewBox="0 0 24 24" fill="none" stroke="#bfbfbf" stroke-width="1.6" aria-hidden="true">
      <circle cx="12" cy="12" r="10"/>
      <path d="M2 12h20M12 2c3 3 3 17 0 20M12 2c-3 3-3 17 0 20"/>
    </svg>
    <div class="contact-web">MARVALEBREEZERENTAL.COM</div>
  </div>
</main>
</body>
</html>
```